Real Estate Sign 2

Our company is called Harwick Tolland Realty. We are a real estate development company. We need a sign that we are going to hang outside of our projects that says: Another project brought to you by Harwick Tolland Realty... For Sale....(213) 555-0847. At the very bottom is needs to say CaBRE# 04736291" We want the Harwick Tolland Realty to be sophisticated, fresh, simple. We do not have a logo so maybe one can be incorporated into the sign. Sign will be about 30"x24"

Industry/Entity Type

Real Estate

```html
<!DOCTYPE html>
<html lang="en">
<head>
<meta charset="utf-8">
<title>Harwick Tolland Realty – For Sale Sign</title>
<link rel="stylesheet" href="https://fonts.googleapis.com/css2?family=EB+Garamond:wght@400&family=Alex+Brush&display=swap">
<style>
  :root {
    --sign-bg: #ffffff;
    --ink: #111111;
    --ink-soft: rgba(17, 17, 17, 0.55);
  }
  html, body {
    margin: 0;
    padding: 0;
    overflow: hidden;
    background: var(--sign-bg);
  }
  .sign {
    position: relative;
    width: 1200px;
    height: 900px;
    background: var(--sign-bg);
    color: var(--ink);
    overflow: hidden;
    font-family: "EB Garamond", Garamond, serif;
  }
  .sign__line {
    position: absolute;
    left: 0;
    width: 100%;
    margin: 0;
    text-align: center;
    line-height: 1;
    font-weight: 400;
    white-space: nowrap;
  }
  .sign__intro {
    top: 122px;
    font-size: 60px;
    padding-left: 24px;
    box-sizing: border-box;
  }
  .sign__company {
    top: 262px;
    font-family: "Alex Brush", cursive;
    font-size: 108px;
  }
  .sign__divider {
    position: absolute;
    left: 405px;
    top: 420px;
    width: 400px;
    height: 56px;
  }
  .sign__status {
    top: 536px;
    font-size: 92px;
  }
  .sign__phone {
    top: 641px;
    font-size: 92px;
  }
  .sign__license {
    top: 815px;
    font-size: 60px;
  }
</style>
</head>
<body>
  <main class="sign">
    <p class="sign__line sign__intro">Another project brought to you by</p>
    <h1 class="sign__line sign__company">Harwick Tolland Realty</h1>

    <svg class="sign__divider" viewBox="0 0 400 56" role="img" aria-label="Decorative calligraphic flourish divider">
      <defs>
        <linearGradient id="flourishTone" x1="0" y1="0" x2="1" y2="0">
          <stop offset="0" stop-color="#111111" stop-opacity="0.05"/>
          <stop offset="0.5" stop-color="#111111" stop-opacity="0.35"/>
          <stop offset="1" stop-color="#111111" stop-opacity="0.05"/>
        </linearGradient>
      </defs>
      <rect x="0" y="8" width="400" height="40" rx="20" fill="url(#flourishTone)"/>
    </svg>

    <p class="sign__line sign__status">For Sale</p>
    <p class="sign__line sign__phone">(213) 555-0847</p>
    <p class="sign__line sign__license">CaBRE# 04736291</p>
  </main>
</body>
</html>
```